Mailing Flyer for Fruit Box Company

Need to design a postcard (2 sides) with both sides completed which will be mailed to companies.

The flyer needs to represent the following point in a graphical way.

1. Our team has sophisticated experience and knowledge in the produce industry that will undoubtedly leave you satisfied.
2. We’ve collaborated with many of our finest local growers that of which have been around for numerous generations such as, Willow Creek Orchards (GIVE MORE LOCAL GROWER EXAMPLES).
3. We have insight on the finest grown fruits; including great judgement as to when they will taste their best.
4. Our company guarantees you get the most superior fruits at the peak of their seasons.
5. With our trustworthy team you can depend on us to satisfy all of your wants and needs.
6. Our farmers grow sustainable produce to help ensure that our future ecosystem is at its absolute best.
7. We have the type of fruits that will not only leave your tastebuds and heart fulfilled, but will cause you to want more after every order.
8. We’ve performed a wholesale business with the farmers in order to grant our customers the freshest fruits at their best valued price.
9. Now that you're able to order from any location in the United States say goodbye to standing in long lines at the grocery stores.
10. Our complementary policy allows our customers to try your first box free of charge.

A summary of the above could be written as:
Our Harvest Rovers Co team has decades of expertise in the produce industry, which we utilize to make insightful decisions on the produce we provide for our customers. We have collaborated with the multi-generational farms such as Willow Creek Orchards to guarantee we supply fruits at the peak of their season. We are an environmentally conscious business, and buy sustainable produce from local growers. When you buy a box from The Harvest Rovers Co you can say goodbye to standing in long lines at the grocery store, enjoy fresh fruit at their best valued price, and receive the first box free of charge.

The point is to illustrate the above, not to have a lot of text since no one reads.
One side is for the mailing so it should have a space to put a sticker for the mailing address to send the mail to.

Size should be 8.5 width x 5.5 high (21.5cm width x 14cm hight)
We will also provide you with the logo of the company (see attached)

Target Market(s)

Offices in the San Francisco Bay Area

Colors

Designer to choose colors to be used in the design.

Requirements
Must have
• Nice photos of Fruits, Fruit boxes, Maybe a nice office meeting room with a nice fruit box on the table, maybe a picture of a beautiful farm. Something inspiring.
• Need to illustrate that products and boxes are delivered to companies.
• Need to give a feeling that this is an Exclusive Service, with the most highest quality fruits and services
• Need to have project in JPG and a format which support edit from our side, with possible layers or vectors.

```html
<!DOCTYPE html>
<html lang="en">
<head>
<meta charset="utf-8">
<title>The Harvest Rovers Co – Postcard</title>
<link rel="stylesheet" href="https://fonts.googleapis.com/css2?family=Arimo:wght@700&display=swap">
<style>
  :root {
    --purple: #8a5a9e;
    --purple-light: #9a68ad;
    --green: #2f9a45;
    --green-light: #5cc052;
    --green-dark: #1f7a35;
    --cloth: #e6a92e;
    --cloth-shade: #c98a1c;
    --kiwi: #8b9a3a;
    --white: #ffffff;
    --ink: #2a5a2a;
  }
  * { margin: 0; padding: 0; box-sizing: border-box; }
  html, body { width: 1200px; height: 781px; overflow: hidden; background: var(--white); }
  .postcard {
    position: relative;
    width: 1200px;
    height: 781px;
    overflow: hidden;
    font-family: "Arimo", Arial, sans-serif;
    font-weight: 700;
    color: var(--white);
    background: linear-gradient(180deg, var(--purple) 0, var(--purple-light) 295px, var(--green-light) 295px, var(--green) 470px, var(--green-dark) 781px);
  }
  .hero-photo {
    position: absolute;
    left: 0;
    top: 150px;
    width: 1200px;
    height: 340px;
    background:
      radial-gradient(ellipse 230px 130px at 630px 150px, var(--kiwi) 0, var(--kiwi) 60%, transparent 100%),
      linear-gradient(180deg, transparent 0, transparent 130px, var(--cloth) 170px, var(--cloth-shade) 290px, transparent 340px);
  }
  .copy {
    position: absolute;
    font-size: 20.5px;
    line-height: 26px;
  }
  .copy-expertise { left: 84px; top: 80px; width: 420px; }
  .copy-farms { right: 83px; top: 80px; width: 400px; text-align: right; }
  .copy-eco { left: 84px; top: 555px; width: 340px; font-size: 25.5px; line-height: 33px; }
  .copy-offer { right: 83px; top: 537px; width: 340px; text-align: right; font-size: 20.5px; line-height: 26px; }
  .brand-mark {
    position: absolute;
    left: 456px;
    top: 413px;
    width: 290px;
    height: 308px;
    border-radius: 50%;
    background: var(--white);
    display: flex;
    align-items: center;
    justify-content: center;
    text-align: center;
  }
  .brand-name {
    color: var(--ink);
    font-size: 26px;
    line-height: 32px;
    width: 200px;
  }
</style>
</head>
<body>
  <main class="postcard">
    <div class="hero-photo" role="img" aria-label="Photo of a halved kiwi on a golden linen cloth with a white fork piercing one half"></div>

    <p class="copy copy-expertise">Our Harvest Rovers Co team has decades of expertise in the produce industry, which we utilize to make insightful decisions on the produce we provide for our customers.</p>

    <p class="copy copy-farms">We have collaborated with the multi-generational farms such as Willow Creek Orchards to guarantee we supply fruits at the peak of their season.</p>

    <p class="copy copy-eco">We are an environmentally conscious business, and buy sustainable produce from local growers.</p>

    <p class="copy copy-offer">When you buy a box from The Harvest Rovers Co you can say goodbye to standing in long lines at the grocery store, enjoy fresh fruit at their best valued price, and receive the first box free of charge.</p>

    <div class="brand-mark">
      <span class="brand-name">The Harvest Rovers Co</span>
    </div>
  </main>
</body>
</html>
```